Web Design Project

We are an aircraft maintenance company servicing small aircraft - both single and twin engines.
we are new business owners and prior to this, no marketing has been done in the business.
We provide superior workmanship, excellent customer service and are there every step of the way for owners of aircraft from purchase through to all the maintenance required on their aircraft.
We are based in Mackay, Queesland, Australia and can service aircraft from around the country.
We also provide a spray painting service and operate in a large hangar at the General aviation section of Brindle Field airport.
We love our industry and are third generation in the aviation business. Most of our clients are either operating aircraft in tourism or charter/flight schools or are aviation enthusiasts who love flying.
We have both used Joomla before and like this as we can easily update information in it.
We like sections to be Home, About Us, Services/Capability, Gallery and Contact us
Please feel free to get in touch if you require more information or if there is a question you'd like to ask about us.
Our logo is attached. This is about to be changed only slightly but inserting a new aircraft. Our colours are navy, red, white and grey.
We like the idea of a blue background/navy background as this looks good on website and is a good colour for an aviation company.
thanks,
Maren
Target Market(s)
owners/operators of small aircraft within Australia, mostly in Queensland.
Industry/Entity Type
Marketing
Look and feel

```html
<!DOCTYPE html>
<html lang="en">
<head>
<meta charset="utf-8">
<title>About Us – Kestrel Aero Aircraft Maintenance</title>
<link rel="stylesheet" href="https://fonts.googleapis.com/css2?family=Open+Sans:wght@400;600&family=Arimo:wght@400;700&display=swap">
<style>
  :root{
    --red:#e0312b;
    --ink:#333333;
    --heading:#555b61;
    --muted:#666a6e;
    --rule:#e6e6e6;
    --band:#f7f7f7;
    --placeholder:#c8c8c8;
    --placeholder-text:#9b9b9b;
    --footer:#434a54;
    --navy:#2b3a55;
  }
  *{box-sizing:border-box;margin:0;padding:0}
  html,body{width:1107px;height:1200px;overflow:hidden;background:#fff}
  body{font-family:"Arimo",Arial,sans-serif;color:var(--ink);position:relative}

  .site-header{height:138px;position:relative;border-bottom:1px solid var(--rule)}
  .brand{position:absolute;left:14px;top:68px;display:flex;align-items:center;gap:12px}
  .brand-square{width:22px;height:22px;background:var(--navy)}
  .brand-name{font-family:"Open Sans",sans-serif;font-weight:600;font-size:32px;line-height:40px;color:var(--red);letter-spacing:.5px}
  .main-nav{position:absolute;right:0;top:96px;display:flex}
  .main-nav a{font-family:"Open Sans",sans-serif;font-size:14px;color:var(--heading);text-decoration:none;padding:14px 18px 12px;display:block;border-bottom:2px solid transparent;height:42px}
  .main-nav a.active{color:var(--red);border-bottom-color:var(--red)}
  .caret{display:inline-block;width:0;height:0;border-left:4px solid transparent;border-right:4px solid transparent;border-top:4px solid var(--red);vertical-align:middle;margin-left:6px}

  .page-title{height:69px;background:var(--band);border-bottom:1px solid var(--rule);display:flex;align-items:center;justify-content:space-between;padding:0 14px}
  .page-title h1{font-family:"Open Sans",sans-serif;font-weight:400;font-size:29px;color:var(--heading)}
  .breadcrumb{font-size:13px;color:var(--muted)}
  .breadcrumb .sep{color:#bbb;margin:0 6px}
  .breadcrumb .current{color:var(--red)}

  .intro{display:flex;justify-content:space-between;padding:30px 14px 0}
  .intro-text{width:540px;font-size:13px;line-height:20.3px}
  .intro-text p{margin-bottom:9px}
  .ticks{list-style:none;margin-top:12px}
  .ticks li{display:flex;align-items:center;gap:6px;line-height:20.3px}
  .video{width:526px;height:302px;background:linear-gradient(160deg,#6f6658,#a39480 55%,#c3b9a8);border-top:3px solid #111;border-bottom:3px solid #111;margin-top:-6px}

  .team{padding:40px 14px 0}
  .section-title{font-family:"Open Sans",sans-serif;font-weight:400;font-size:24px;color:var(--heading);border-bottom:1px solid var(--rule);padding-bottom:2px}
  .section-title span{display:inline-block;border-bottom:2px solid var(--red);margin-bottom:-1px}
  .team-grid{display:flex;justify-content:space-between;padding:34px 11px 0}
  .member{width:227px}
  .photo{height:173px;background:var(--placeholder);display:flex;align-items:center;justify-content:center;font-family:"Open Sans",sans-serif;font-size:22px;color:var(--placeholder-text)}
  .member h3{font-family:"Open Sans",sans-serif;font-weight:400;font-size:19px;color:var(--heading);margin-top:14px}
  .role{font-family:"Open Sans",sans-serif;font-size:11px;color:var(--ink);margin-top:2px}
  .bio{font-size:13px;line-height:20.3px;margin-top:10px}
  .social{display:flex;justify-content:flex-end;gap:3px;margin-top:6px}
  .social span{width:26px;height:26px;background:#f2f2f2;display:flex;align-items:center;justify-content:center}
  .social span i{width:10px;height:10px;background:#b5b5b5;display:block}

  .site-footer{position:absolute;left:0;top:1024px;width:100%;height:51px;background:var(--footer);color:#e8e8e8;font-size:11px;display:flex;align-items:center;padding:0 14px}
</style>
</head>
<body>
  <header class="site-header">
    <div class="brand">
      <div class="brand-square"></div>
      <div class="brand-name">KESTREL AERO</div>
    </div>
    <nav class="main-nav">
      <a href="#">HOME</a>
      <a href="#" class="active">ABOUT US</a>
      <a href="#">SERVICES<span class="caret"></span></a>
      <a href="#">GALLERY</a>
      <a href="#">CONTACT US</a>
    </nav>
  </header>

  <section class="page-title">
    <h1>About Us</h1>
    <div class="breadcrumb">Home<span class="sep">/</span><span class="current">About Us</span></div>
  </section>

  <section class="intro">
    <div class="intro-text">
      <p>Lorem ipsum dolor sit amet, consectetur adipiscing duis mollis, est non commodo luctus elit posuere erat a ante. Aenean eu leo quam. Pellentesque ornare sem lacinia quam venenatis lorem ipsum dolor sit amet, consectetur adipiscing. Pellentesque ornare sem lacinia quam venenatis lorem ipsum dolor sit amet, consectetur adipiscingsit amet. Lorem ipsum dolor sit amet consectetur.</p>
      <p>Donec id elit non mi porta gravida at eget metus. Pellentesque ornare sem lacinia quam venenatis lorem ipsum dolor sit amet, consectetur adipiscing. Pellentesque ornare sem lacinia quam venenatis lorem ipsum dolor sit amet, consectetur adipiscingsit amet.</p>
      <ul class="ticks">
        <li><svg width="12" height="10" viewBox="0 0 12 10"><path d="M1 5l3.5 3.5L11 1.5" fill="none" stroke="#e0312b" stroke-width="2.4"/></svg>Lorem ipsum dolor sit amet</li>
        <li><svg width="12" height="10" viewBox="0 0 12 10"><path d="M1 5l3.5 3.5L11 1.5" fill="none" stroke="#e0312b" stroke-width="2.4"/></svg>Consectetur adipiscing elit</li>
        <li><svg width="12" height="10" viewBox="0 0 12 10"><path d="M1 5l3.5 3.5L11 1.5" fill="none" stroke="#e0312b" stroke-width="2.4"/></svg>Integer molestie lorem at massa</li>
        <li><svg width="12" height="10" viewBox="0 0 12 10"><path d="M1 5l3.5 3.5L11 1.5" fill="none" stroke="#e0312b" stroke-width="2.4"/></svg>Facilisis in pretium nisl aliquet</li>
        <li><svg width="12" height="10" viewBox="0 0 12 10"><path d="M1 5l3.5 3.5L11 1.5" fill="none" stroke="#e0312b" stroke-width="2.4"/></svg>Nulla volutpat aliquam velit</li>
      </ul>
    </div>
    <div class="video" role="img" aria-label="Embedded video of a construction site with excavators and vehicles"></div>
  </section>

  <section class="team">
    <h2 class="section-title"><span>Meet Our Team</span></h2>
    <div class="team-grid">
      <article class="member">
        <div class="photo">760 x 580</div>
        <h3>Fred Bloggs</h3>
        <div class="role">Chief Executive Officer</div>
        <p class="bio">Donec id elit non mi porta gravida at eget metus. Fusce dapibus, justo sit amet risus etiam porta sem...</p>
        <div class="social"><span><i></i></span><span><i></i></span><span><i></i></span></div>
      </article>
      <article class="member">
        <div class="photo">760 x 580</div>
        <h3>Mrs Kafoops</h3>
        <div class="role">Chief Operating Officer</div>
        <p class="bio">Donec id elit non mi porta gravida at eget metus. Fusce dapibus, justo sit amet risus etiam porta sem...</p>
        <div class="social"><span><i></i></span><span><i></i></span><span><i></i></span></div>
      </article>
      <article class="member">
        <div class="photo">760 x 580</div>
        <h3>Tommy Atkins</h3>
        <div class="role">Financial Controller/Quality Manager</div>
        <p class="bio">Donec id elit non mi porta gravida at eget metus. Fusce dapibus, justo sit amet risus etiam porta sem...</p>
        <div class="social"><span><i></i></span><span><i></i></span><span><i></i></span></div>
      </article>
      <article class="member">
        <div class="photo">760 x 580</div>
        <h3>John Doe</h3>
        <div class="role">Safety Manager</div>
        <p class="bio">Donec id elit non mi porta gravida at eget metus. Fusce dapibus, justo sit amet risus etiam porta sem...</p>
        <div class="social"><span><i></i></span><span><i></i></span><span><i></i></span></div>
      </article>
    </div>
  </section>

  <footer class="site-footer">Copyright © 2013 Kestrel Aero Aircraft Maintenance. All rights reserved.</footer>
</body>
</html>
```